Pest Control Company needs business card!

Hi there, we need a business card designed for our new Pest Control Company. Ideally this card will be simple, yet feel elegant and high end. We want to use the colours Orange, Black and White. Please see our attached logo for the exact colours.

Business card details:

Phone - 0461 275 804
Name - Gavin Holloway
Email - Info@steadfastverminguard.com.au

We would also like to include the following list with dot points:

SERVICES / INSPECTIONS

Termites, Wood Borers, Ants, Cockroaches, Spiders, Fleas, Mice, Rats, Bed Bugs, & More!

```html
<!DOCTYPE html>
<html lang="en">
<head>
<meta charset="utf-8">
<title>Steadfast Vermin Guard – Business Card</title>
<link rel="stylesheet" href="https://fonts.googleapis.com/css2?family=Roboto:ital,wght@0,400;0,700;0,900;1,400&display=swap">
<style>
  :root {
    --stage: #2b2b2b;
    --card: #1e1e1e;
    --orange: #f7861f;
    --white: #f4f4f4;
    --icon-red: #e0312b;
  }
  * { margin: 0; padding: 0; box-sizing: border-box; }
  html, body {
    width: 1200px; height: 900px; overflow: hidden;
    background: var(--stage);
    font-family: "Roboto", sans-serif;
  }
  .sheet {
    width: 1200px; height: 900px;
    display: flex; flex-direction: column;
    align-items: center; justify-content: center; gap: 46px;
  }
  .card {
    position: relative;
    width: 660px; height: 377px;
    background: var(--card);
    border-radius: 3px;
    box-shadow: 0 10px 30px rgba(0,0,0,.45);
    overflow: hidden;
  }
  .brand {
    display: flex; align-items: center; gap: 14px;
    color: var(--orange);
    font-weight: 900; text-transform: uppercase;
    line-height: 1.02; letter-spacing: .5px;
  }
  .brand-dot { border-radius: 50%; background: var(--orange); flex: none; }

  /* front */
  .card-front .brand {
    position: absolute; top: 62px; left: 150px;
    font-size: 40px;
  }
  .card-front .brand-dot { width: 88px; height: 88px; }
  .services {
    position: absolute; left: 58px; right: 40px; top: 232px;
    color: var(--white);
    font-size: 17px; letter-spacing: .6px; line-height: 1.55;
    text-transform: uppercase;
  }
  .services .sep { color: var(--orange); margin: 0 6px; }

  /* back */
  .card-back .brand {
    position: absolute; top: 40px; left: 52px;
    font-size: 26px;
  }
  .card-back .brand-dot { width: 52px; height: 52px; }
  .divider {
    position: absolute; left: 52px; right: 52px; top: 212px;
    height: 1.5px; background: var(--orange);
  }
  .holder {
    position: absolute; right: 52px; top: 150px; text-align: right;
  }
  .holder-name {
    color: var(--orange); font-weight: 900; font-size: 25px;
    text-transform: uppercase; letter-spacing: .5px;
  }
  .holder-role { color: var(--white); font-style: italic; font-size: 17px; margin-top: 2px; }
  .contacts {
    position: absolute; left: 52px; top: 232px;
    list-style: none; color: var(--white); font-size: 16px;
  }
  .contacts li { display: flex; align-items: center; gap: 10px; margin-bottom: 8px; }
  .contacts svg { width: 14px; height: 14px; fill: var(--icon-red); flex: none; }
</style>
</head>
<body>
<main class="sheet">
  <section class="card card-front" aria-label="Card front">
    <div class="brand">
      <span class="brand-dot"></span>
      <span>Steadfast<br>Vermin<br>Guard</span>
    </div>
    <p class="services">
      Termites<span class="sep">•</span>Wood Borers<span class="sep">•</span>Ants<span class="sep">•</span>Cockroaches<br>
      Spiders<span class="sep">•</span>Fleas<span class="sep">•</span>Mice<span class="sep">•</span>Rats<span class="sep">•</span>Bed Bugs<span class="sep">•</span>&amp; More!
    </p>
  </section>

  <section class="card card-back" aria-label="Card back">
    <div class="brand">
      <span class="brand-dot"></span>
      <span>Steadfast<br>Vermin Guard</span>
    </div>
    <div class="holder">
      <p class="holder-name">Gavin Holloway</p>
      <p class="holder-role">President</p>
    </div>
    <div class="divider"></div>
    <ul class="contacts">
      <li>
        <svg viewBox="0 0 24 24" aria-hidden="true"><path d="M6.6 10.8a15.1 15.1 0 0 0 6.6 6.6l2.2-2.2a1 1 0 0 1 1-.25 11.4 11.4 0 0 0 3.6.57 1 1 0 0 1 1 1V20a1 1 0 0 1-1 1A17 17 0 0 1 3 4a1 1 0 0 1 1-1h3.5a1 1 0 0 1 1 1c0 1.25.2 2.45.57 3.6a1 1 0 0 1-.25 1z"/></svg>
        0461 275 804
      </li>
      <li>
        <svg viewBox="0 0 24 24" aria-hidden="true"><path d="M2 5h20v14H2zm2 2v.5l8 5 8-5V7l-8 5z"/></svg>
        Info@steadfastverminguard.com.au
      </li>
      <li>
        <svg viewBox="0 0 24 24" aria-hidden="true"><path d="M12 2a10 10 0 1 0 0 20 10 10 0 0 0 0-20zm6.9 6h-3a15 15 0 0 0-1.3-3.9A8 8 0 0 1 18.9 8zM12 4a13 13 0 0 1 1.9 4h-3.8A13 13 0 0 1 12 4zM4.3 14a8 8 0 0 1 0-4h3.3a16 16 0 0 0 0 4zm.8 2h3a15 15 0 0 0 1.3 3.9A8 8 0 0 1 5.1 16zm3-8h-3a8 8 0 0 1 4.3-3.9A15 15 0 0 0 8.1 8zM12 20a13 13 0 0 1-1.9-4h3.8A13 13 0 0 1 12 20zm2.3-6H9.7a14 14 0 0 1 0-4h4.6a14 14 0 0 1 0 4zm.3 5.9a15 15 0 0 0 1.3-3.9h3a8 8 0 0 1-4.3 3.9zm1.8-5.9a16 16 0 0 0 0-4h3.3a8 8 0 0 1 0 4z"/></svg>
        www.steadfastverminguard.com.au
      </li>
    </ul>
  </section>
</main>
</body>
</html>
```